Individual Brochures for 6 products

Urgent request need this in 2 days thank you.

I need 2 fold Brochure (W:20XH:23) simple brochures (individual) for 6 products the overall look is white, clean with a touch of metalic red and black. I included photos of each products and description in folder. This is for Medical Clinic so make the design more medical and clean

files can be found from filevaultly link below

https://www.filevaultly.net/sh/7ruq3pkw0zemtx/BBF2HqNsWTaLcKyPmReDjXntu?dl=0

Note: file i have attach below is size i want for the brochure. The design and photos are on the filevaultly link above.

Thank you in advance for rushing this project

Target Market(s)

Aesthetic, beauty industry

Industry/Entity Type

Medical

Font styles to use
Other font styles liked:
• Velora - Roboto, UPR- Bangla MN

Colors
ffffff
ec1f27

Requirements
Must have
• photo of a lady in each brochures (different product different photos) see photos in filevaultly link
• https://www.filevaultly.net/sh/w8k396nydt214pe/BBF_qusTXpJvLmR3HeZ9WcbNx?dl=0

```html
<!DOCTYPE html>
<html lang="en">
<head>
<meta charset="utf-8">
<title>UPR Bi-fold Brochure</title>
<link rel="stylesheet" href="https://fonts.googleapis.com/css2?family=Cinzel:wght@400;700&family=Roboto:wght@400;500&display=swap">
<style>
  :root {
    --brand-red: #ec1f27;
    --bright-red: #ff0a0a;
    --ink: #1c1c1c;
    --white: #ffffff;
    --panel-grey: #e9e9ea;
    --silver-dark: #8e8e90;
    --silver-light: #e4e4e6;
    --stage: #e7e8eb;
  }
  html, body {
    margin: 0;
    padding: 0;
    width: 751px;
    height: 1200px;
    overflow: hidden;
    background: var(--stage);
  }
  .brochure {
    position: absolute;
    left: 25px;
    top: 250px;
    width: 700px;
    height: 700px;
    box-shadow: 0 6px 18px rgba(0,0,0,0.18);
  }
  .wordmark { font-family: "Roboto", sans-serif; font-weight: 400; fill: var(--ink); letter-spacing: 2px; }
  .headline { font-family: "Cinzel", serif; font-weight: 400; fill: var(--brand-red); font-size: 17px; letter-spacing: 0.3px; }
  .contact-title { font-family: "Roboto", sans-serif; font-weight: 400; fill: var(--white); font-size: 14px; letter-spacing: 0.2px; }
  .contact-detail { font-family: "Roboto", sans-serif; font-weight: 400; fill: var(--white); font-size: 8.5px; }
  .cover-blurb { font-family: "Roboto", sans-serif; font-weight: 500; fill: var(--white); font-size: 10.5px; }
  .web-pill-text { font-family: "Cinzel", serif; font-weight: 700; fill: var(--brand-red); font-size: 10.5px; }
</style>
</head>
<body>
<svg class="brochure" viewBox="0 0 624 624" xmlns="http://www.w3.org/2000/svg">
  <defs>
    <linearGradient id="back-panel" x1="0" y1="0" x2="1" y2="0">
      <stop offset="0" stop-color="#ffffff"/>
      <stop offset="1" stop-color="#e9e9ea"/>
    </linearGradient>
    <linearGradient id="photo-tones" x1="0" y1="0" x2="1" y2="1">
      <stop offset="0" stop-color="#f3eef2"/>
      <stop offset="0.35" stop-color="#e9c9d6"/>
      <stop offset="0.6" stop-color="#dcb39a"/>
      <stop offset="1" stop-color="#e8e4e8"/>
    </linearGradient>
    <linearGradient id="headline-fade" x1="0" y1="0" x2="1" y2="0">
      <stop offset="0" stop-color="#ffffff" stop-opacity="0.95"/>
      <stop offset="0.75" stop-color="#ffffff" stop-opacity="0.9"/>
      <stop offset="1" stop-color="#ffffff" stop-opacity="0.6"/>
    </linearGradient>
    <linearGradient id="silver" x1="0" y1="0" x2="1" y2="0">
      <stop offset="0" stop-color="#e4e4e6"/>
      <stop offset="0.4" stop-color="#8e8e90"/>
      <stop offset="0.7" stop-color="#d6d6d8"/>
      <stop offset="1" stop-color="#8e8e90"/>
    </linearGradient>
    <linearGradient id="red-band" x1="0" y1="0" x2="1" y2="0">
      <stop offset="0" stop-color="#ff0a0a"/>
      <stop offset="1" stop-color="#ec1f27"/>
    </linearGradient>
  </defs>

  <rect class="back-panel" x="0" y="0" width="312" height="624" fill="url(#back-panel)"/>

  <g role="img" aria-label="Photo of a woman in profile with pink magnolia blossoms">
    <rect x="312" y="0" width="312" height="530" fill="url(#photo-tones)"/>
  </g>

  <path class="silver-swoosh" d="M0,486 C120,438 240,412 330,416 C430,420 520,504 580,504 C600,504 615,484 624,470 L624,624 L0,624 Z" fill="url(#silver)"/>
  <path class="red-base" d="M0,500 C120,458 240,430 330,434 C430,438 520,522 580,522 C600,522 615,502 624,490 L624,624 L0,624 Z" fill="url(#red-band)"/>

  <text class="wordmark" x="156" y="322" font-size="34" text-anchor="middle">UPR</text>

  <text class="wordmark" x="330" y="74" font-size="46">UPR</text>

  <rect class="headline-box" x="312" y="290" width="168" height="128" fill="url(#headline-fade)"/>
  <text class="headline">
    <tspan x="332" y="325">LOREM</tspan>
    <tspan x="332" y="347">IPSUM</tspan>
    <tspan x="332" y="368">DOLOR SIT</tspan>
    <tspan x="332" y="390">AMET, CONSE</tspan>
    <tspan x="332" y="411">CTETUR ADIPIS</tspan>
  </text>

  <text class="contact-title" x="156" y="569" text-anchor="middle">CONTACT US TODAY</text>
  <g class="contact-detail-row">
    <path d="M19,589 a2.4,2.4 0 1,1 4.8,0 c0,2 -2.4,4.4 -2.4,4.4 s-2.4,-2.4 -2.4,-4.4z" fill="var(--white)"/>
    <text class="contact-detail"><tspan x="27" y="594">418 N. Larkin Ave.</tspan><tspan x="27" y="604">Dunmore Vale, PA 18519</tspan></text>
    <path d="M132,595 h6 v3 h-6z M133,593 h4 v2 h-4z" fill="var(--white)"/>
    <text class="contact-detail" x="144" y="599">123-456-789</text>
    <rect x="210" y="588" width="6" height="4" fill="var(--white)"/>
    <text class="contact-detail" x="222" y="593">info@website.com</text>
    <circle cx="213" cy="601" r="2.6" fill="var(--white)"/>
    <text class="contact-detail" x="222" y="604">www.website.com</text>
  </g>

  <text class="cover-blurb" text-anchor="middle">
    <tspan x="468" y="561">EXCEPTEUR SINT OCCAECAT CUPIDATAT NON</tspan>
    <tspan x="468" y="573">PROIDENT, SUNT IN CULPA QUI OFFICIA DESERUNT</tspan>
    <tspan x="468" y="585">MOLLIT ANIM ID EST LABORUM.</tspan>
  </text>

  <path class="web-pill" d="M395,624 V610 a4,4 0 0 1 4,-4 H538 a4,4 0 0 1 4,4 V624 Z" fill="var(--white)"/>
  <text class="web-pill-text" x="468" y="619" text-anchor="middle">WWW.WEBSITE.COM</text>
</svg>
</body>
</html>
```